Pruitt Denatl Laboratory nees a window design

We want to make a window cover 8 feet wide and 6 feet tall to advertise our dental lab with all the products we produce<br/>: Digital Cad/Cam<br/>: Implants<br/>: Dentures<br/>: Cast Partials <br/>: Orthodontic appliances<br/><br/> and it has to include a service we provide for a denturist on site by appointment only.<br/><br/>Please use the sample logo below our colours are white backround and blue letters

Font styles to use
Script

Colors
ffffff
0355a3

Requirements
Nice to have
• a picture of a teddy bear on a dental chair, or some dental work particularly bridge work since our moto is Building bridges since 1976
Should not have
• real people

```html
<!DOCTYPE html>
<html lang="en">
<head>
<meta charset="utf-8">
<title>Pruitt Denatl Laboratory – Window Cover</title>
<link rel="stylesheet" href="https://fonts.googleapis.com/css2?family=Allura&family=Roboto:ital,wght@1,700;1,900&display=swap">
<style>
  :root {
    --page-bg: #eef1f4;
    --sheet-white: #ffffff;
    --brand-blue: #1f7cc4;
    --brand-deep: #0355a3;
    --band-start: #2f6dbd;
    --band-end: #2cb9ec;
    --photo-deep: #1d4f86;
    --photo-mid: #3f86c4;
    --photo-soft: #8fb8dc;
  }
  html, body {
    margin: 0;
    padding: 0;
    width: 975px;
    height: 1200px;
    overflow: hidden;
    background: var(--page-bg);
  }
  .canvas {
    width: 975px;
    height: 1200px;
    display: flex;
    align-items: center;
    justify-content: center;
  }
  .window-cover {
    width: 975px;
    height: 731px;
    display: block;
    background: var(--sheet-white);
    box-shadow: 0 2px 6px rgba(0,0,0,0.18);
  }
  .brand-name {
    font-family: "Allura", cursive;
    font-weight: 400;
    font-size: 68px;
    fill: var(--brand-blue);
  }
  .tagline {
    font-family: "Roboto", Arial, sans-serif;
    font-style: italic;
    font-weight: 700;
    font-size: 20px;
    fill: var(--brand-blue);
  }
  .products-title {
    font-family: "Roboto", Arial, sans-serif;
    font-style: italic;
    font-weight: 900;
    font-size: 42px;
    fill: var(--sheet-white);
  }
  .product-item {
    font-family: "Roboto", Arial, sans-serif;
    font-style: italic;
    font-weight: 700;
    font-size: 33px;
    fill: var(--sheet-white);
  }
  .service-note {
    font-family: "Roboto", Arial, sans-serif;
    font-style: italic;
    font-weight: 700;
    font-size: 21px;
    fill: var(--brand-blue);
  }
</style>
</head>
<body>
<main class="canvas">
  <svg class="window-cover" viewBox="0 0 975 731" xmlns="http://www.w3.org/2000/svg">
    <defs>
      <linearGradient id="band-gradient" x1="0" y1="0" x2="1" y2="0">
        <stop offset="0" stop-color="var(--band-start)"/>
        <stop offset="1" stop-color="var(--band-end)"/>
      </linearGradient>
      <linearGradient id="photo-gradient" x1="0" y1="0" x2="1" y2="1">
        <stop offset="0" stop-color="var(--photo-deep)"/>
        <stop offset="0.5" stop-color="var(--photo-soft)"/>
        <stop offset="1" stop-color="var(--photo-mid)"/>
      </linearGradient>
    </defs>

    <g class="brand-header">
      <circle cx="100" cy="115" r="30" fill="var(--brand-blue)"/>
      <text class="brand-name" x="158" y="140">Pruitt Denatl Laboratory</text>
    </g>

    <g class="tagline-block">
      <text class="tagline" x="923" y="86" text-anchor="end">BUILDING BRIDGES</text>
      <text class="tagline" x="923" y="114" text-anchor="end">SINCE 1976</text>
    </g>

    <path class="product-band"
      d="M0,318 C120,240 300,205 470,270 C540,298 600,360 640,440 L640,700 C520,705 420,640 300,600 C190,565 90,555 0,560 Z"
      fill="url(#band-gradient)"/>

    <path class="photo-arc"
      d="M540,210 C650,130 860,125 975,170 L975,205 C860,160 680,165 580,230 Z"
      fill="var(--brand-blue)"/>

    <path class="hero-photo" role="img"
      aria-label="Photo of a patient having a dental check-up with a gloved dentist"
      d="M580,230 C680,165 860,160 975,205 L975,640 C900,690 760,710 540,707 C460,610 470,360 580,230 Z"
      fill="url(#photo-gradient)"/>

    <path class="swoosh-line"
      d="M0,325 C110,265 270,250 400,305 C520,355 595,480 595,707"
      fill="none" stroke="var(--sheet-white)" stroke-width="3"/>

    <g class="products">
      <text class="products-title" x="55" y="345">PRODUCTS</text>
      <text class="product-item" x="55" y="395">• Digital Cad/Cam</text>
      <text class="product-item" x="55" y="435">• Implants</text>
      <text class="product-item" x="55" y="475">• Dentures</text>
      <text class="product-item" x="55" y="515">• Cast Partials</text>
      <text class="product-item" x="55" y="555">• Orthodontic appliances</text>
    </g>

    <g class="service-note-block">
      <text class="service-note" x="50" y="625">We provide</text>
      <text class="service-note" x="50" y="651">a services for</text>
      <text class="service-note" x="50" y="677">denturist on site by</text>
      <text class="service-note" x="50" y="703">appointment only</text>
    </g>
  </svg>
</main>
</body>
</html>
```